German CBD company needs a label+packaging design (templates provided)

Hey there,
we are a German e-commerce company and about to launch a CBD E-liquid series under our new brand "QUELVINA". We need designs for the cardbord tube packaging and the labels of bottles. Find attached templates for both, the labels and the packaging. The templates already have a design on them just for you to know that some space will be filled with legal information. Feel free to use the templates and change the designs and of course we have the suitable text down below. Every outer packaging label and bottle label should include the brand name "QUELVINA" (we typically use the font Archivo Black, but feel free to change it, if you have a better idea), the CBD content, the flavour and the filling quantity (10ml). You can use 100mg and Mango for your design and if your design wins, we will work with you and change the flavours and concentrations for the other liquids accordingly. Our liquids are Made in Germany and of a very high quality so we are looking for a premium design that underlines the quality und purity of our product. Something between luxurious and futuristic. Please let your creativity run wild :)

As for the packaging we need the following texts on the packaging:

DE:
(bold)Inhaltsstoffe:(bold) < 70% Propylen Glycol, < 30% VG Glycerol, Aromen, Cannabidiol (CBD) wie angegeben CAS 13956-29-1.
(bold)Anwendung(bold) Vor Benutzung schütteln. Dieses Produkt ist unverdünnt in einer kompatiblen e-Zigarette anzuwenden. 2-3 Züge inhalieren. Zwischen den Anwendungen 10-20 Minuten warten. Dieses Produkt ersetzt keine ausgewogene Ernährung.
(bold)Hinweise:(bold) QUELVINA CBD e-Liquids sind Tabakersatzprodukte gem. TPD2 und bestehen aus organischen und zertifizierten, >99% reinen CBD-Kristallen. HACCP & GMP konform. Nicht empfohlen für Schwangere, stillende Frauen oder Nichtraucher. Dieses Produkt ist nicht zur Diagnose, Behandlung, Heilung oder Vorbeugung von Krankheiten bestimmt. Darf nicht in die Hände von Kindern und Jugendlichen gelangen. Keine Abgabe unter 18 Jahren. Dunkel und kühl lagern. Nicht zum Verzehr geeignet.

EN:
(bold)Ingredients:(bold) < 70% Propylen Glycol, < 30% VG Glycerol, flavours , Cannabidiol (CBD).
(bold)Application(bold): Shake before use. This product should be applied undiluted in a compatible e-cigarette. Inhale 2-3 puffs. Wait 10-20 minutes until using again.
(bold)Notes(bold): QUELVINA e-liquids are made from organic and certified >99% pure CBD Crystals. HACCP & GMP compliant. Not recommended for pregnant or breastfeeding women or non-smokers.
This product is not intended to diagnose, treat, cure or prevent any disease. Keep away from children. No sale to minors. Store in a cool, dark place. Not for consumption.

DE: Qualität:
Wir verwenden für unsere Liquids organische und zertifizierte CBD-Kristalle von >99% Reinheit. Wir verwenden nur die hochwertigsten Rohstoffe zur Herstellung unserer Liquids, um unseren Kunden ein optimales Vape-Erlebnis bieten zu können.
EN: Quality:
We use organic and certified CBD-Crystals with a purity >99%. We only use the highest quality raw material for the production of our liquids in order to ensure an optimal vaping experience for our customers.

Please consider that we will also need space for our contact information, our website URL and an EAN bar code.

Now the label for the bottles: As already said our templates have designs on them, so please feel free to change anything you like. It`s just an example of the label printing company so we could get an idea. We just need the following texts on those labels:
DE:(bold)Inhaltsstoffe:(bold) < 70% Propylen Glycol, < 30% VG Glycerol, Aromen, Cannabidiol (CBD) wie angegeben CAS 13956-29-1.
Darf nicht in die Hände von Kindern und Jugendlichen gelangen. Keine Abgabe unter 18 Jahren.

EN:(bold)Ingredients:(bold) < 70% Propylen Glycol, < 30% VG Glycerol, flavours , Cannabidiol (CBD).
Keep away from children. No sale to minors.
Moreover, we need the symbols that are already on the label and some space for an EAN bar code. The labels should include CBD content, brand name, flavour..(see above)

I hope our briefing is clear enough. If you have any further questions, please contact me via e-mail (ole.vardek@brovatt-online.com).
We are looking forwards to receiving your designs and doing some further work with you. We know that it`s more than one simple task, so we are willing to pay a little bonus for the further work which we will do with the winner :)

Greetings from Frankfurt, Germany
Brovatt GmbH Team
Ole Vardek
ole.vardek@brovatt-online.com

attachments:
cbd25 = picture of bottle with label
tube = outer packaging
korin-cbd-label-25-DE = template for the label on the bottle
tube-small-korin-label-eliquid-25mg-DE = template for outer packaging label

• Archivo Black (not mandatory, just an idea)

• - Legal notices as mentioned above
• - CBD content in mg
• - flavour
• - space for EAN bar code & contact information
• - shouldn`t look too clean, not like a medicine

```html
<!DOCTYPE html>
<html lang="en">
<head>
<meta charset="utf-8">
<title>QUELVINA – CBD E-Liquid Labels and Tubes</title>
<link rel="stylesheet" href="https://fonts.googleapis.com/css2?family=Archivo+Black&family=PT+Sans:ital,wght@0,400;0,700;1,700&display=swap">
<style>
  :root {
    --page: #ffffff;
    --stage: #e7e7e7;
    --paper: #ffffff;
    --ink: #1b1d18;
    --mango: #c8ab38;
    --melon: #a12b52;
    --disc-grey: #7c7c7c;
    --disc-black: #0b0b0b;
    --line: #ffffff;
  }
  * { box-sizing: border-box; margin: 0; padding: 0; }
  html, body {
    width: 927px; height: 1200px; overflow: hidden;
    background: var(--page);
  }
  .sheet { position: relative; width: 927px; height: 1200px; }

  .stage {
    position: absolute; width: 362px;
    background: var(--stage);
  }
  .stage--top { top: 120px; height: 440px; }
  .stage--bottom { top: 602px; height: 478px; }
  .stage--left { left: 94px; }
  .stage--right { left: 472px; }

  .mango { --flavour: var(--mango); }
  .melon { --flavour: var(--melon); }

  /* Bottle label */
  .bottle-label {
    position: absolute; left: 51px; top: 70px;
    width: 260px; height: 300px;
    background: var(--paper);
  }
  .bottle-label__brand {
    height: 70px; display: flex; align-items: center; justify-content: center;
    font-family: "Archivo Black", sans-serif; font-size: 24px; font-weight: 400;
    letter-spacing: 3px; color: var(--ink);
  }
  .bottle-label__band { display: block; background: var(--flavour); }

  /* Tube wrap */
  .tube-wrap {
    position: absolute; left: 31px; top: 28px;
    width: 300px; height: 422px;
    background: var(--paper);
  }
  .tube-wrap__brand {
    height: 90px; display: flex; align-items: center; justify-content: center;
    font-family: "Archivo Black", sans-serif; font-size: 27px; font-weight: 400;
    letter-spacing: 5px; color: var(--ink);
  }
  .tube-wrap__band { display: block; background: var(--flavour); }
  .tube-wrap__info {
    display: grid; grid-template-columns: 1fr 1fr; gap: 18px;
    padding: 12px 10px 0;
  }
  .quality {
    font-family: "PT Sans", sans-serif; font-size: 6.2px; line-height: 1.4;
    color: var(--ink); font-weight: 700;
  }
  .quality--en { text-align: right; font-style: italic; padding-top: 18px; }

  .label-text { font-family: "PT Sans", sans-serif; fill: var(--line); }
  .label-heavy { font-family: "Archivo Black", sans-serif; fill: var(--line); }
</style>
</head>
<body>
<main class="sheet">

  <!-- Bottle label: Mango -->
  <section class="stage stage--top stage--left mango">
    <article class="bottle-label">
      <h1 class="bottle-label__brand">QUELVINA</h1>
      <svg class="bottle-label__band" width="260" height="230" viewBox="0 0 260 230">
        <g fill="none" stroke="#fff" stroke-width="2">
          <rect x="8" y="20" width="92" height="32"/>
          <rect x="104" y="20" width="144" height="32"/>
          <rect x="8" y="56" width="92" height="52"/>
          <line x1="8" y1="104" x2="100" y2="60"/>
          <rect x="8" y="170" width="92" height="32"/>
          <rect x="104" y="56" width="144" height="146"/>
        </g>
        <text class="label-text" x="54" y="43" font-size="15" text-anchor="middle" letter-spacing="1">100 MG</text>
        <text class="label-text" x="176" y="42" font-size="12" text-anchor="middle" letter-spacing=".5">CBD E-LIQUID</text>
        <text class="label-text" x="12" y="74" font-size="11">99%</text>
        <text class="label-text" x="96" y="100" font-size="11" text-anchor="end">PURE</text>
        <text class="label-text" x="54" y="132" font-size="12" text-anchor="middle">FULL</text>
        <text class="label-text" x="54" y="150" font-size="12" text-anchor="middle">SPECTRUM</text>
        <text class="label-text" x="54" y="192" font-size="12" text-anchor="middle">ORGANIC</text>
        <circle cx="176" cy="129" r="46" fill="var(--disc-grey)"/>
        <text class="label-text" x="176" y="133" font-size="12" font-weight="700" text-anchor="middle" letter-spacing="1.5">MANGO</text>
        <text class="label-text" x="176" y="221" font-size="7" text-anchor="middle" letter-spacing=".5">0.3 FL OZ  /  10 ML</text>
      </svg>
    </article>
  </section>

  <!-- Bottle label: Watermelon -->
  <section class="stage stage--top stage--right melon">
    <article class="bottle-label">
      <h1 class="bottle-label__brand">QUELVINA</h1>
      <svg class="bottle-label__band" width="260" height="230" viewBox="0 0 260 230">
        <g fill="none" stroke="#fff" stroke-width="2">
          <rect x="8" y="20" width="92" height="32"/>
          <rect x="104" y="20" width="144" height="32"/>
          <rect x="8" y="56" width="92" height="52"/>
          <line x1="8" y1="104" x2="100" y2="60"/>
          <rect x="8" y="170" width="92" height="32"/>
          <rect x="104" y="56" width="144" height="146"/>
        </g>
        <text class="label-text" x="54" y="43" font-size="15" text-anchor="middle" letter-spacing="1">100 MG</text>
        <text class="label-text" x="176" y="42" font-size="12" text-anchor="middle" letter-spacing=".5">CBD E-LIQUID</text>
        <text class="label-text" x="12" y="74" font-size="11">99%</text>
        <text class="label-text" x="96" y="100" font-size="11" text-anchor="end">PURE</text>
        <text class="label-text" x="54" y="132" font-size="12" text-anchor="middle">FULL</text>
        <text class="label-text" x="54" y="150" font-size="12" text-anchor="middle">SPECTRUM</text>
        <text class="label-text" x="54" y="192" font-size="12" text-anchor="middle">ORGANIC</text>
        <circle cx="176" cy="129" r="46" fill="var(--disc-grey)"/>
        <text class="label-text" x="176" y="125" font-size="12" font-weight="700" text-anchor="middle" letter-spacing="1.5">WATER</text>
        <text class="label-text" x="176" y="141" font-size="12" font-weight="700" text-anchor="middle" letter-spacing="1.5">MELON</text>
        <text class="label-text" x="176" y="221" font-size="7" text-anchor="middle" letter-spacing=".5">0.3 FL OZ  /  10 ML</text>
      </svg>
    </article>
  </section>

  <!-- Tube wrap: Mango -->
  <section class="stage stage--bottom stage--left mango">
    <article class="tube-wrap">
      <h1 class="tube-wrap__brand">QUELVINA</h1>
      <svg class="tube-wrap__band" width="300" height="210" viewBox="0 0 300 210">
        <text class="label-text" x="150" y="28" font-size="13" font-weight="700" text-anchor="middle" letter-spacing="2">0.3 FL OZ  /  10 ML</text>
        <g fill="none" stroke="#fff" stroke-width="2">
          <rect x="40" y="40" width="100" height="38"/>
          <rect x="140" y="48" width="124" height="34"/>
          <line x1="140" y1="78" x2="140" y2="196"/>
          <rect x="40" y="150" width="100" height="34"/>
          <line x1="264" y1="82" x2="264" y2="196"/>
          <line x1="0" y1="196" x2="300" y2="196"/>
          <line x1="0" y1="204" x2="300" y2="204"/>
        </g>
        <text class="label-text" x="90" y="64" font-size="11" font-weight="700" text-anchor="middle" letter-spacing="1">100 MG</text>
        <text class="label-text" x="202" y="70" font-size="11" font-weight="700" text-anchor="middle" letter-spacing="1">CBD E-LIQUID</text>
        <text class="label-heavy" x="56" y="108" font-size="12" letter-spacing="2">99%</text>
        <text class="label-heavy" x="52" y="132" font-size="14" letter-spacing="3">PURE</text>
        <text class="label-text" x="90" y="172" font-size="11" font-weight="700" text-anchor="middle" letter-spacing="1">ORGANIC</text>
        <circle cx="202" cy="140" r="46" fill="var(--disc-black)"/>
        <text class="label-heavy" x="202" y="144" font-size="10" text-anchor="middle" letter-spacing="2">MANGO</text>
      </svg>
      <div class="tube-wrap__info">
        <p class="quality quality--de">Wir verwenden für unsere Liquids organische und zertifizierte CBD-Kristalle von &gt;99% Reinheit. Wir verwenden nur die hochwertigsten Rohstoffe zur Herstellung unserer Liquids, um unseren Kunden ein optimales Vape-Erlebnis bieten zu können.</p>
        <p class="quality quality--en">We use organic and certified CBD-Crystals with a purity &gt;99%. We only use the highest quality raw material for the production of our liquids in order to ensure an optimal vaping experience for our customers.</p>
      </div>
    </article>
  </section>

  <!-- Tube wrap: Watermelon -->
  <section class="stage stage--bottom stage--right melon">
    <article class="tube-wrap">
      <h1 class="tube-wrap__brand">QUELVINA</h1>
      <svg class="tube-wrap__band" width="300" height="210" viewBox="0 0 300 210">
        <text class="label-text" x="150" y="28" font-size="13" font-weight="700" text-anchor="middle" letter-spacing="2">0.3 FL OZ  /  10 ML</text>
        <g fill="none" stroke="#fff" stroke-width="2">
          <rect x="40" y="40" width="100" height="38"/>
          <rect x="140" y="48" width="124" height="34"/>
          <line x1="140" y1="78" x2="140" y2="196"/>
          <rect x="40" y="150" width="100" height="34"/>
          <line x1="264" y1="82" x2="264" y2="196"/>
          <line x1="0" y1="196" x2="300" y2="196"/>
          <line x1="0" y1="204" x2="300" y2="204"/>
        </g>
        <text class="label-text" x="90" y="64" font-size="11" font-weight="700" text-anchor="middle" letter-spacing="1">100 MG</text>
        <text class="label-text" x="202" y="70" font-size="11" font-weight="700" text-anchor="middle" letter-spacing="1">CBD E-LIQUID</text>
        <text class="label-heavy" x="56" y="108" font-size="12" letter-spacing="2">99%</text>
        <text class="label-heavy" x="52" y="132" font-size="14" letter-spacing="3">PURE</text>
        <text class="label-text" x="90" y="172" font-size="11" font-weight="700" text-anchor="middle" letter-spacing="1">ORGANIC</text>
        <circle cx="202" cy="140" r="46" fill="var(--disc-black)"/>
        <text class="label-heavy" x="202" y="143" font-size="8" text-anchor="middle" letter-spacing="1">WATERMELON</text>
      </svg>
      <div class="tube-wrap__info">
        <p class="quality quality--de">Wir verwenden für unsere Liquids organische und zertifizierte CBD-Kristalle von &gt;99% Reinheit. Wir verwenden nur die hochwertigsten Rohstoffe zur Herstellung unserer Liquids, um unseren Kunden ein optimales Vape-Erlebnis bieten zu können.</p>
        <p class="quality quality--en">We use organic and certified CBD-Crystals with a purity &gt;99%. We only use the highest quality raw material for the production of our liquids in order to ensure an optimal vaping experience for our customers.</p>
      </div>
    </article>
  </section>

</main>
</body>
</html>
```